依頼詳細
このもんじゃ焼き店の店頭入り口の上に設置する看板のデザインのご提案をお願いいたします。
和モダン・高級感・シンプルをイメージしています。
参考までに、店舗の内装はエボニー(彩協会番号25-30B)・ナバホホワイト(22-85D)の2トーンです。

納品データについては下記のご対応をお願いいたしますので予めご了承ください。
・サイズは変更になる可能性があり、デザイン選定後に調整のお願いをする場合があります
・印刷会社指定の入稿用データの作成をお願いいたします
記載項目
【デザインについて】
・クリーム系(暖色系)の白ベースに右端の方に店名を入れていただきたいです
(電光看板で中に昼光色の蛍光灯を設置するので、点灯した際に看板が暖色系の白・クリーム色にしたいため)
・店頭幕を設置予定(画像参照)のため、店頭幕や店頭と雰囲気を合わせていただきたいです
・各パネルの間に柱があり、現在は赤色(画像参照)ですがデザインいただいた地の色に近い色で塗装しますので、考慮いただきデザイン制作をお願いいたします
・提案いただく際に、本募集に添付する画像を使用した店頭設置イメージをつけていただけると選考がスムーズになり大変助かります

店舗名:もんじゃ焼 梅ころ
サイズ:W5400mm×H640mm
※納品いただく5データは下記のサイズになります。
W1800×H640 ×1
W900×H640× 4

【納品データについて】
・実際の看板は柱ごとに別のパネルのため5枚に分かれています(画像参照)
・納品データは上記5データで作成をお願いいたします
希望イメージ
シンプル 複雑
単色 カラフル
暗い 明るい
日常 高級
遊び心 厳粛
未来的 伝統的
女性的 男性的
希望する色
茶系、無彩色系
納品ファイル
• 高解像度JPG (.jpg)
• イラストレーター形式 (.ai)
• PNG形式 (.png)
補足説明
デザインへの要望を追加し、締め切り日時を1日延長いたします。

【デザインへの要望】
募集開始時に添付した画像のとおり、既存看板は5つに分かれており、
各看板の間にある枠は撤去できないのでこの構成自体を変えることはできません。
(5つに分かれているものを3つや1つにまとめる、各パネルのサイズを変えるなどはできません)
しかし、デザインは、5つ分割でなく、できるだけ1つにまとまったように見えるものが理想です。
そのため、各パネルの間にある枠は、採用させていただくデザインのベースの色に近い色で塗装する予定でおります。(各パネルの間にある枠を分からないようにするため)
ややこしくて申し訳ありませんが、
5つのブロックを強調せずに、1ブロックに見えるようなデザインを希望しております。

ご不明点等ありましたらメッセージでご連絡ください。
■ 選んだ理由

店舗イメージに合ったデザインを採用させていただきました。

■ 提案者全員のお礼・コメント

この度はたくさんのご提案をいただき誠にありがとうございました。
今後も機会がありましたらご参加いただけますと幸いです。

```html
<!DOCTYPE html>
<html lang="ja">
<head>
<meta charset="utf-8">
<title>もんじゃ焼 梅ころ 看板 カラー案</title>
<link href="https://fonts.googleapis.com/css2?family=Kaisei+Tokumin:wght@800&family=Noto+Sans+JP:wght@400&display=swap" rel="stylesheet">
<style>
  :root{
    --paper:#ffffff;
    --label:#333333;
    --cream:#f4ecd2;
    --kuro:#0c0b0a;
    --kurocha:#3b2314;
    --sabitetsu:#6a392d;
  }
  *{box-sizing:border-box;margin:0;padding:0}
  html,body{width:848px;height:1200px;overflow:hidden;background:var(--paper)}
  .sheet{position:relative;width:848px;height:1200px}
  .variant{position:absolute;left:27px;width:794px}
  .variant-label{
    font-family:"Noto Sans JP",sans-serif;font-weight:400;font-size:16px;color:var(--label);
    height:22px;line-height:22px;margin-bottom:2px
  }
  .sign{display:flex;gap:3px;height:62px;margin-bottom:70px}
  .panel{
    display:flex;align-items:center;justify-content:center;gap:3px;
    background:var(--base);color:var(--cream);overflow:hidden;
    font-family:"Kaisei Tokumin",serif;font-weight:800;font-size:30px;line-height:1;white-space:nowrap
  }
  .panel-1{width:132px}
  .panel-2{width:124px}
  .panel-3{width:262px}
  .panel-4{width:138px;font-size:28px}
  .panel-5{width:126px;gap:6px}
  .spatula{width:12px;height:26px;background:var(--cream);clip-path:polygon(0 0,100% 0,100% 45%,60% 100%,35% 100%,0 45%)}
  .bamboo{width:34px;height:40px;background:linear-gradient(160deg,rgba(244,236,210,.55),rgba(244,236,210,.15));border-radius:3px}
  .shop-name{font-size:16px;writing-mode:vertical-rl;letter-spacing:1px;line-height:1}
  .kuro{--base:var(--kuro);top:160px}
  .kurocha{--base:var(--kurocha);top:514px}
  .sabitetsu{--base:var(--sabitetsu);top:910px}
</style>
</head>
<body>
<main class="sheet">

  <section class="variant kuro">
    <h2 class="variant-label">黒</h2>
    <div class="sign">
      <div class="panel panel-1">お好み</div>
      <div class="panel panel-2">焼き<span class="spatula" role="img" aria-label="へらのイラスト"></span></div>
      <div class="panel panel-3">もんじゃ焼き<span class="spatula" role="img" aria-label="へらのイラスト"></span></div>
      <div class="panel panel-4">鉄板焼き</div>
      <div class="panel panel-5"><span class="bamboo" role="img" aria-label="笹のイラスト"></span><span class="shop-name">梅ころ</span></div>
    </div>
    <div class="sign">
      <div class="panel panel-1">お好み</div>
      <div class="panel panel-2">焼き<span class="spatula" role="img" aria-label="へらのイラスト"></span></div>
      <div class="panel panel-3">もんじゃ焼き<span class="spatula" role="img" aria-label="へらのイラスト"></span></div>
      <div class="panel panel-4">鉄板焼き</div>
      <div class="panel panel-5"><span class="bamboo" role="img" aria-label="笹のイラスト"></span><span class="shop-name">梅ころ</span></div>
    </div>
  </section>

  <section class="variant kurocha">
    <h2 class="variant-label">黒茶</h2>
    <div class="sign">
      <div class="panel panel-1">お好み</div>
      <div class="panel panel-2">焼き<span class="spatula" role="img" aria-label="へらのイラスト"></span></div>
      <div class="panel panel-3">もんじゃ焼き<span class="spatula" role="img" aria-label="へらのイラスト"></span></div>
      <div class="panel panel-4">鉄板焼き</div>
      <div class="panel panel-5"><span class="bamboo" role="img" aria-label="笹のイラスト"></span><span class="shop-name">梅ころ</span></div>
    </div>
    <div class="sign">
      <div class="panel panel-1">お好み</div>
      <div class="panel panel-2">焼き<span class="spatula" role="img" aria-label="へらのイラスト"></span></div>
      <div class="panel panel-3">もんじゃ焼き<span class="spatula" role="img" aria-label="へらのイラスト"></span></div>
      <div class="panel panel-4">鉄板焼き</div>
      <div class="panel panel-5"><span class="bamboo" role="img" aria-label="笹のイラスト"></span><span class="shop-name">梅ころ</span></div>
    </div>
  </section>

  <section class="variant sabitetsu">
    <h2 class="variant-label">錆鉄</h2>
    <div class="sign">
      <div class="panel panel-1">お好み</div>
      <div class="panel panel-2">焼き<span class="spatula" role="img" aria-label="へらのイラスト"></span></div>
      <div class="panel panel-3">もんじゃ焼き<span class="spatula" role="img" aria-label="へらのイラスト"></span></div>
      <div class="panel panel-4">鉄板焼き</div>
      <div class="panel panel-5"><span class="bamboo" role="img" aria-label="笹のイラスト"></span><span class="shop-name">梅ころ</span></div>
    </div>
  </section>

</main>
</body>
</html>
```